Nimbrel Computer Solutions
Business Technology Consulting
Professional
Gerald Pinto
1837 NE 41st Court
Palm Hollow, FL 33990
gerald@nimbrelcs.com
www.nimbrelcs.com
My company file logo. Please contact me if another format is needed.

```html
<!DOCTYPE html>
<html lang="en">
<head>
<meta charset="utf-8">
<title>Nimbrel Computer Solutions – Stationery Set</title>
<link rel="stylesheet" href="https://fonts.googleapis.com/css2?family=Open+Sans:wght@300;400;600;700;800&display=swap">
<style>
  :root{
    --navy:#17386f;
    --gold:#c9a227;
    --gold-soft:#e2c35a;
    --paper:#ffffff;
    --ink:#3b4350;
    --muted:#8a919c;
    --line:#d5d9df;
    --cell:#f2f4f7;
    --backdrop:#e7e9ec;
  }
  *{box-sizing:border-box;margin:0;padding:0}
  html,body{width:1200px;height:864px;overflow:hidden}
  body{background:var(--backdrop);font-family:"Open Sans",Arial,sans-serif;color:var(--ink);position:relative}
  .sheet{position:absolute;background:var(--paper);box-shadow:0 3px 10px rgba(0,0,0,.12);overflow:hidden}
  .sheet > *{position:relative;z-index:1}
  .sheet > .swoosh,.sheet > .faint-circle{position:absolute;z-index:0;pointer-events:none}
  .brand{display:flex;align-items:center;gap:6px}
  .brand-dot{width:16px;height:16px;border-radius:50%;background:var(--navy);flex:none}
  .brand-name{font-weight:800;color:var(--navy);font-size:13px;line-height:1.1}
  .tagline{font-size:6.5px;letter-spacing:1.2px;text-transform:uppercase;color:var(--gold);font-weight:600;margin-top:3px;margin-left:22px}
  .faint-circle{border-radius:50%;background:var(--navy);opacity:.05}
  .small{font-size:6.5px;line-height:1.55;color:var(--ink)}

  /* Letterhead */
  .letterhead{left:40px;top:40px;width:340px;height:480px;padding:26px 28px}
  .letter-body{margin-top:34px;font-size:6.5px;line-height:1.7}
  .letter-body p{margin-bottom:8px}
  .signature{font-weight:700;color:var(--navy);margin-top:18px}
  .letter-footer{position:absolute !important;left:28px;bottom:22px;font-size:6px;line-height:1.6;color:var(--muted)}

  /* Fax */
  .fax{left:400px;top:40px;width:340px;height:480px;padding:26px 28px}
  .fax-head{display:flex;justify-content:space-between;align-items:flex-start}
  .fax-title{font-size:20px;font-weight:300;letter-spacing:3px;color:var(--navy);line-height:1}
  .fax-table{margin-top:36px;width:100%;border-collapse:collapse;font-size:6.5px}
  .fax-table td{border-bottom:1px solid var(--line);padding:7px 4px}
  .fax-table td.label{font-weight:700;color:var(--navy);width:16%;background:var(--cell)}
  .fax-checks{display:flex;gap:14px;margin-top:14px;font-size:6.5px}
  .fax-checks span::before{content:"";display:inline-block;width:6px;height:6px;border:1px solid var(--navy);margin-right:4px;vertical-align:-1px}

  /* Business cards */
  .card{width:350px;height:200px}
  .card-front{left:790px;top:40px;padding:22px 24px}
  .card-name{margin-top:40px;font-size:13px;font-weight:700;color:var(--navy)}
  .card-role{font-size:7px;color:var(--gold);font-weight:600;letter-spacing:1px;text-transform:uppercase;margin-bottom:10px}
  .card-back{left:790px;top:262px;background:var(--navy);display:flex;flex-direction:column;align-items:center;justify-content:center}
  .card-back .brand-dot{background:var(--gold);width:22px;height:22px}
  .card-back .brand-name{color:#fff;font-size:17px}
  .card-back .tagline{margin-left:0;margin-top:6px;color:var(--gold-soft)}

  /* Envelope */
  .envelope{left:40px;top:560px;width:560px;height:264px;padding:24px 26px}
  .envelope-return{margin-top:8px;margin-left:22px}

  /* Compliments slip */
  .compliments{left:640px;top:560px;width:500px;height:264px;padding:24px 26px}
  .compliments-title{margin-top:60px;font-size:15px;font-weight:300;color:var(--navy);letter-spacing:1px}
  .compliments-contact{position:absolute !important;left:26px;bottom:22px;font-size:6px;color:var(--muted);line-height:1.6}
</style>
</head>
<body>

<section class="sheet letterhead">
  <div class="faint-circle" style="width:200px;height:200px;left:70px;top:250px"></div>
  <svg class="swoosh" style="right:0;bottom:0" width="340" height="160" viewBox="0 0 340 160">
    <path d="M340 20 C300 90 230 140 110 160 L340 160 Z" fill="var(--gold)"/>
    <path d="M340 50 C310 110 250 148 170 160 L340 160 Z" fill="var(--navy)"/>
  </svg>
  <div class="brand"><span class="brand-dot"></span><span class="brand-name">Nimbrel Computer Solutions</span></div>
  <div class="tagline">Business Technology Consulting</div>
  <div class="letter-body">
    <p>Recipient Name<br>Company<br>Street Address<br>City, State ZIP</p>
    <p>Dear Recipient,</p>
    <p>Thank you for choosing us to support your business technology. Our team reviews every system with care and plans upgrades that fit your goals and budget.</p>
    <p>We will contact you this week to schedule a visit and confirm the next steps for your office network.</p>
    <p>Sincerely,</p>
    <p class="signature">Gerald Pinto</p>
  </div>
  <div class="letter-footer">1837 NE 41st Court, Palm Hollow, FL 33990<br>gerald@nimbrelcs.com · www.nimbrelcs.com</div>
</section>

<section class="sheet fax">
  <div class="faint-circle" style="width:200px;height:200px;left:70px;top:240px"></div>
  <svg class="swoosh" style="right:0;bottom:0" width="340" height="140" viewBox="0 0 340 140">
    <path d="M340 30 C300 90 240 125 150 140 L340 140 Z" fill="var(--gold)"/>
  </svg>
  <div class="fax-head">
    <div>
      <div class="brand"><span class="brand-dot"></span><span class="brand-name">Nimbrel Computer Solutions</span></div>
      <div class="tagline">Business Technology Consulting</div>
    </div>
    <div class="fax-title">FAX</div>
  </div>
  <table class="fax-table">
    <tr><td class="label">To</td><td></td><td class="label">From</td><td></td></tr>
    <tr><td class="label">Fax</td><td></td><td class="label">Pages</td><td></td></tr>
    <tr><td class="label">Phone</td><td></td><td class="label">Date</td><td></td></tr>
    <tr><td class="label">Re</td><td></td><td class="label">CC</td><td></td></tr>
  </table>
  <div class="fax-checks"><span>Urgent</span><span>For Review</span><span>Please Comment</span><span>Please Reply</span></div>
</section>

<section class="sheet card card-front">
  <svg class="swoosh" style="right:0;top:0" width="120" height="200" viewBox="0 0 120 200">
    <path d="M120 0 L40 0 C80 50 95 130 70 200 L120 200 Z" fill="var(--gold)"/>
    <path d="M120 0 L60 0 C100 50 112 130 92 200 L120 200 Z" fill="var(--navy)"/>
  </svg>
  <div class="brand"><span class="brand-dot"></span><span class="brand-name">Nimbrel Computer Solutions</span></div>
  <div class="card-name">Gerald Pinto</div>
  <div class="card-role">Principal Consultant</div>
  <div class="small">1837 NE 41st Court<br>Palm Hollow, FL 33990<br>T: (239) 555-0148<br>gerald@nimbrelcs.com<br>www.nimbrelcs.com</div>
</section>

<section class="sheet card card-back">
  <svg class="swoosh" style="left:0;bottom:0" width="350" height="60" viewBox="0 0 350 60">
    <path d="M0 60 C120 20 240 10 350 30 L350 60 Z" fill="var(--gold)" opacity=".9"/>
  </svg>
  <div class="brand"><span class="brand-dot"></span><span class="brand-name">Nimbrel Computer Solutions</span></div>
  <div class="tagline">Business Technology Consulting</div>
</section>

<section class="sheet envelope">
  <svg class="swoosh" style="left:0;top:0" width="560" height="264" viewBox="0 0 560 264">
    <path d="M0 264 L0 150 C120 130 220 100 300 40 C220 120 120 180 0 264 Z" fill="var(--gold)"/>
    <path d="M0 264 L0 180 C110 165 200 130 270 80 C200 150 110 215 0 264 Z" fill="var(--navy)"/>
  </svg>
  <div class="brand"><span class="brand-dot"></span><span class="brand-name">Nimbrel Computer Solutions</span></div>
  <div class="tagline">Business Technology Consulting</div>
  <div class="small envelope-return">1837 NE 41st Court, Palm Hollow, FL 33990</div>
</section>

<section class="sheet compliments">
  <div class="faint-circle" style="width:180px;height:180px;left:200px;top:60px"></div>
  <svg class="swoosh" style="right:0;top:0" width="160" height="264" viewBox="0 0 160 264">
    <path d="M160 0 L70 0 C120 70 130 170 90 264 L160 264 Z" fill="var(--gold)"/>
    <path d="M160 0 L95 0 C140 70 150 170 118 264 L160 264 Z" fill="var(--navy)"/>
  </svg>
  <div class="brand"><span class="brand-dot"></span><span class="brand-name">Nimbrel Computer Solutions</span></div>
  <div class="tagline">Business Technology Consulting</div>
  <div class="compliments-title">With Compliments</div>
  <div class="compliments-contact">1837 NE 41st Court, Palm Hollow, FL 33990<br>gerald@nimbrelcs.com · www.nimbrelcs.com</div>
</section>

</body>
</html>
```